Responsive HomePage and InnerPage Design and HTML/CSS/JS Needed for the AI/Data Analysis Industry

I have an existing website and I am looking to redesign the HTML and layout of the homepage and menu to look more polished and robust. The website's existing homepage is at https://trackmindlens.example. The finished HTML/CSS/JS deliverable should be responsive down to mobile and include my new logo and a YouTube video to open in a modal window. It should look very professional and polished using the existing menu infrastructure. The color scheme and NEXA font should be used for all submitted designs should follow the attached branding guidelines.

Target Market(s)

Data Analytics Professionals and Users

Industry/Entity Type

AI/Data Analysis

Coding

Number of Pages Required

2 page

Font styles to use
Other font styles liked:
• NEXA PRO

Requirements
Must have
• Responsiveness for large screens down to tablet and cell phone and follow the guidelines in the branding document provided.
Nice to have
• High converting design
Should not have
• Lots of whitespace in the design; Unresponsiveness; Poor Color Scheme that doesn't follow branding guide provided

```html
<!DOCTYPE html>
<html lang="en">
<head>
<meta charset="utf-8">
<title>TrackMind Lens</title>
<link href="https://fonts.googleapis.com/css2?family=Montserrat:wght@400;500;600;700&family=Roboto:wght@400;500&display=swap" rel="stylesheet">
<style>
:root{
  --navy:#1d1850;
  --navy-deep:#0f1433;
  --hero:#0b2446;
  --orange:#ef7326;
  --red:#ee3b48;
  --ink:#1a1f3a;
  --muted:#666a78;
  --line:#e6e6ec;
  --white:#ffffff;
}
*{box-sizing:border-box;margin:0;padding:0}
html,body{width:1200px;height:4666px;overflow:hidden}
body{font-family:"Roboto",Arial,sans-serif;color:var(--ink);background:var(--white);position:relative}
h1,h2,h3,h4,.head{font-family:"Montserrat",Arial,sans-serif}

/* header */
.site-header{position:absolute;top:0;left:0;width:1200px;height:100px;background:var(--white);z-index:5}
.topbar{position:absolute;left:345px;top:0;width:855px;height:46px;background:linear-gradient(90deg,var(--orange),var(--red));clip-path:polygon(28px 0,100% 0,100% 100%,0 100%)}
.topbar .item{position:absolute;top:10px;display:flex;align-items:center;gap:12px;color:var(--white);font-size:14px}
.topbar .ico{width:30px;height:30px;border-radius:50%;background:var(--white);display:flex;align-items:center;justify-content:center}
.social{display:flex;gap:14px}
.social span{width:28px;height:28px;border-radius:50%;background:var(--white);display:block}
.topbar .social{position:absolute;left:593px;top:9px}
.brand{position:absolute;left:96px;top:30px;display:flex;align-items:center;gap:10px;font-family:"Montserrat",sans-serif;font-weight:700;font-size:19px;color:var(--navy)}
.brand i{width:16px;height:16px;border-radius:50%;background:var(--red);display:block}
.nav{position:absolute;top:65px;left:453px;display:flex;gap:45px;font-size:15px;color:var(--ink)}

/* hero */
.hero{position:absolute;top:100px;left:0;width:1200px;height:660px}
.hero-edge{position:absolute;inset:0;background:var(--orange);clip-path:polygon(0 0,100% 0,100% 540px,50% 660px,0 540px)}
.hero-bg{position:absolute;inset:0;background:radial-gradient(circle at 52% 62%,#f6d7b0 0,#7a5a57 8%,#1a4a74 22%,var(--hero) 55%);clip-path:polygon(0 0,100% 0,100% 515px,50% 640px,0 510px)}
.hero-text{position:absolute;top:90px;width:100%;text-align:center;color:var(--white)}
.hero-text p{font-family:"Montserrat",sans-serif;font-weight:600;font-size:20px;letter-spacing:1px}
.hero-text h1{font-size:60px;font-weight:700;margin-top:14px;letter-spacing:1px}

/* mission */
.card-mv{position:absolute;top:843px;width:474px;height:330px;border-radius:14px;color:var(--white);text-align:center;padding:38px 22px 0;box-shadow:0 8px 22px rgba(0,0,0,.12)}
.card-mv.mission{left:98px;background:var(--orange)}
.card-mv.vision{left:628px;background:var(--red);padding-top:36px}
.badge{width:100px;height:100px;border-radius:50%;background:var(--white);margin:0 auto 22px;display:flex;align-items:center;justify-content:center}
.card-mv h3{font-size:21px;font-weight:700;margin-bottom:18px}
.card-mv p{font-size:14.5px;line-height:31px}

/* about */
.about{position:absolute;top:1287px;left:0;width:1200px;height:661px;background:var(--navy)}
.about-visual{position:absolute;left:120px;top:110px;width:450px;height:450px;border-radius:50%;border:5px solid var(--white);background:radial-gradient(circle,#4ad0f0 0,#3a5bd0 30%,#1f2a6a 60%,#0c1440 100%)}
.about-copy{position:absolute;left:628px;top:98px;width:470px;color:var(--white)}
.about-copy h2{font-size:34px;font-weight:700}
.about-copy .rule{width:52px;height:3px;background:var(--white);margin:14px 0 24px}
.about-copy p{font-size:14.5px;line-height:31px}
.btn-light{display:inline-block;margin-top:26px;background:var(--white);color:var(--navy);font-family:"Montserrat",sans-serif;font-weight:700;font-size:14.5px;padding:12px 27px;border-radius:24px}

/* section titles */
.sec-title{position:absolute;width:100%;text-align:center;font-size:33px;font-weight:700;color:var(--navy)}
.sec-mark{position:absolute;left:583px;width:34px;height:20px}

/* faq */
.faq-item{position:absolute;left:127px;width:946px;border:2px solid var(--line);border-radius:30px;background:var(--white)}
.faq-item .row{display:flex;align-items:center;height:58px;padding:0 28px 0 22px}
.faq-item .q{width:38px;height:38px;border-radius:50%;background:#fde4e3;color:var(--ink);font-family:"Montserrat",sans-serif;font-weight:600;font-size:15px;display:flex;align-items:center;justify-content:center;margin-right:26px}
.faq-item.open .q{background:var(--red);color:var(--white)}
.faq-item .t{flex:1;font-family:"Montserrat",sans-serif;font-size:16px;font-weight:500}
.faq-item .pm{font-size:22px;font-weight:700}
.faq-item .a{padding:0 60px 22px 86px;font-size:14px;line-height:30px;color:var(--muted)}

/* analyze */
.analyze{position:absolute;top:2751px;left:0;width:1200px;height:733px;background:linear-gradient(90deg,var(--orange),var(--red))}
.analyze .sec-title{color:var(--white);top:120px}
.tool{position:absolute;top:208px;width:467px;height:418px;background:var(--white);border-radius:12px;padding:20px}
.tool .pic{height:323px;border-radius:10px}
.tool h3{text-align:center;font-size:19px;font-weight:600;margin-top:28px;color:var(--ink)}

/* blog */
.post{position:absolute;top:3687px;width:310px;height:434px;background:var(--white);border:1px solid var(--line);box-shadow:0 4px 14px rgba(0,0,0,.06)}
.post .pic{height:165px;position:relative;background:linear-gradient(135deg,#c9d3dc,#8a9aa8 55%,#59677a)}
.post .date{position:absolute;left:22px;bottom:-2px;background:var(--navy);color:var(--white);font-family:Georgia,serif;font-size:14px;padding:8px 22px}
.post h3{font-size:21px;font-weight:500;line-height:30px;margin:32px 22px 0;color:var(--ink)}
.post p{font-size:13.5px;line-height:30px;color:var(--muted);margin:20px 22px 0}

/* footer */
.footer{position:absolute;top:4217px;left:0;width:1200px;height:449px;background:var(--navy-deep);color:var(--white)}
.footer h4{font-size:23px;font-weight:500;position:absolute;top:62px}
.links{position:absolute;left:98px;top:112px;list-style:none;font-size:14px}
.links li{height:31px;display:flex;align-items:center;gap:10px}
.footer .social{position:absolute;left:98px;top:338px;gap:18px}
.footer .social span{background:var(--red);width:30px;height:30px}
.divider{position:absolute;top:100px;height:260px;border-left:1px dashed rgba(255,255,255,.45)}
.contact{position:absolute;left:355px;width:240px;display:flex;gap:14px}
.contact .ic{width:32px;height:32px;border-radius:50%;background:var(--red);flex:none;display:flex;align-items:center;justify-content:center}
.contact b{font-size:15px;display:block;margin-bottom:10px}
.contact span{font-size:14px}
.contact-sep{position:absolute;left:355px;width:240px;border-top:1px dashed rgba(255,255,255,.5)}
.form{position:absolute;left:717px;top:104px;width:352px}
.field{height:38px;border:1px solid rgba(255,255,255,.8);margin-bottom:15px;padding:0 10px;display:flex;align-items:center;font-size:13px}
.submit{height:36px;background:var(--red);display:flex;align-items:center;justify-content:center;font-size:15px;font-weight:500}
.copy{position:absolute;left:98px;top:383px;width:1004px;border-top:1px solid rgba(255,255,255,.6);text-align:center;padding-top:26px;font-size:14px}
</style>
</head>
<body>

<header class="site-header">
  <div class="brand"><i></i>TRACKMIND LENS</div>
  <div class="topbar">
    <div class="item" style="left:105px">
      <span class="ico"><svg width="14" height="14" viewBox="0 0 24 24"><path fill="#ef5a3a" d="M6.6 10.8a15 15 0 0 0 6.6 6.6l2.2-2.2c.3-.3.7-.4 1-.2 1.1.4 2.3.6 3.6.6.6 0 1 .4 1 1V20c0 .6-.4 1-1 1A17 17 0 0 1 3 4c0-.6.4-1 1-1h3.5c.6 0 1 .4 1 1 0 1.3.2 2.5.6 3.6.1.3 0 .7-.2 1z"/></svg></span>+1 555 0142 7788</div>
    <div class="item" style="left:333px">
      <span class="ico"><svg width="14" height="14" viewBox="0 0 24 24"><path fill="#ef5a3a" d="M3 5h18v14H3z M3 5l9 7 9-7" stroke="#fff" stroke-width="1.5"/></svg></span>info@trackmindlens.example</div>
    <div class="social" aria-label="Social links"><span></span><span></span><span></span><span></span></div>
  </div>
  <nav class="nav"><span>Home</span><span>Analyze Log Files</span><span>Subscribe</span><span>About Us</span><span>FAQ</span><span>Contact Us</span></nav>
</header>

<section class="hero">
  <div class="hero-edge"></div>
  <div class="hero-bg" role="img" aria-label="Robotic hand and human hand reaching toward a glowing point of light over circuit graphics"></div>
  <div class="hero-text"><p>WELCOME TO</p><h1>TRACKMIND LENS</h1></div>
</section>

<article class="card-mv mission">
  <div class="badge"><svg width="50" height="50" viewBox="0 0 50 50" fill="none" stroke="#1a1f3a" stroke-width="2.5"><circle cx="22" cy="28" r="16"/><circle cx="22" cy="28" r="9"/><circle cx="22" cy="28" r="2.5"/><path d="M22 28 40 10M36 8l4 2 2 4"/></svg></div>
  <h3>OUR MISSION</h3>
  <p>Our mission is to revolutionize log analysis using cutting-edge Generative AI, simplifying the extraction of meaningful insights from diverse log formats.</p>
</article>
<article class="card-mv vision">
  <div class="badge"><svg width="50" height="50" viewBox="0 0 50 50" fill="none" stroke="#1a1f3a" stroke-width="2.5"><path d="M25 10a12 12 0 0 0-7 22v5h14v-5a12 12 0 0 0-7-22z"/><path d="M20 41h10M25 2v4M8 10l3 3M42 10l-3 3M4 24h4M46 24h-4"/></svg></div>
  <h3>OUR VISION</h3>
  <p>Our vision is to be the forefront provider, enabling organizations to make informed decisions, proactively address challenges, and optimize system performance advanced log analysis solutions.</p>
</article>

<section class="about">
  <div class="about-visual" role="img" aria-label="Glowing blue AI emblem with artificial intelligence wave graphic"></div>
  <div class="about-copy">
    <h2>ABOUT US</h2>
    <div class="rule"></div>
    <p>Meet our founder, Daniel Rowe, a passionate data analyst who has spent his entire career unraveling the complex mysteries hidden within data. Daniel's journey in data analysis was sparked by an early fascination with the infinite possibilities of data interpretation. He realized the enormous potential of transforming raw, seemingly chaotic data into meaningful information that can drive decision-making processes and strategies. With this conviction, he channeled his passion and expertise into creating TrackMind Lens, a platform that embodies his love for data analysis and his commitment to making this power accessible to all.</p>
    <span class="btn-light">Read More</span>
  </div>
</section>

<svg class="sec-mark" style="top:2033px" viewBox="0 0 34 20" fill="none" stroke="#ee3b48" stroke-width="2"><path d="M2 10h30M10 4l6 6-6 6M24 4l-6 6 6 6"/></svg>
<h2 class="sec-title" style="top:2072px">FAQ</h2>

<div class="faq-item" style="top:2147px"><div class="row"><span class="q">Q</span><span class="t">1. WHAT IS TRACKMINDLENS?</span><span class="pm">+</span></div></div>
<div class="faq-item" style="top:2235px"><div class="row"><span class="q">Q</span><span class="t">2. WHICH FILE FORMATS DOES TRACKMINDLENS SUPPORT?</span><span class="pm">+</span></div></div>
<div class="faq-item open" style="top:2323px"><div class="row"><span class="q">Q</span><span class="t">3. HOW DOES TRACKMINDLENS ANALYZE LOG FILES?</span><span class="pm">&minus;</span></div>
  <p class="a">TrackMindLens uses sophisticated GPT-based algorithms to read and analyze the contents of your log files. It identifies patterns, anomalies, and provides comprehensive reports based on the file data.</p></div>
<div class="faq-item" style="top:2497px"><div class="row"><span class="q">Q</span><span class="t">4. IS TRACKMINDLENS FREE TO USE?</span><span class="pm">+</span></div></div>
<div class="faq-item" style="top:2585px"><div class="row"><span class="q">Q</span><span class="t">5. HOW DO I USE TRACKMINDLENS?</span><span class="pm">+</span></div></div>

<section class="analyze">
  <svg class="sec-mark" style="top:92px" viewBox="0 0 34 20" fill="none" stroke="#fff" stroke-width="2"><path d="M2 10h30M10 4l6 6-6 6M24 4l-6 6 6 6"/></svg>
  <h2 class="sec-title">ANALYZE LOG FILES</h2>
  <div class="tool" style="left:115px"><div class="pic" role="img" aria-label="Laptop with magnifying glass and alert symbol on a dark blue tech background" style="background:radial-gradient(circle at 50% 50%,#8fd0ff 0,#3a4aa8 35%,#141a4a 80%)"></div><h3>STANDARD FILE ANALYSIS</h3></div>
  <div class="tool" style="left:620px"><div class="pic" role="img" aria-label="Analyst holding a laptop in front of a bright growth chart" style="background:linear-gradient(120deg,#e9eef3,#c9d6e2 50%,#9fc0e4)"></div><h3>INTERACTIVE FILE ANALYSIS</h3></div>
</section>

<svg class="sec-mark" style="top:3574px" viewBox="0 0 34 20" fill="none" stroke="#ee3b48" stroke-width="2"><path d="M2 10h30M10 4l6 6-6 6M24 4l-6 6 6 6"/></svg>
<h2 class="sec-title" style="top:3612px">LATEST BLOG</h2>

<article class="post" style="left:111px"><div class="pic" role="img" aria-label="Team discussing work around an office table"><span class="date">12 Jan 2024</span></div><h3>Sed ut perspiciatis unde omnis</h3><p>Ut enim ad minima veniam, quis nostrum exercitationem ullamtu corporis suscipit laboriosam, utt nisi ut aliquid ex ea commod.</p></article>
<article class="post" style="left:445px"><div class="pic" role="img" aria-label="Two colleagues reviewing a document in a bright office"><span class="date">12 Jan 2024</span></div><h3>Sed ut perspiciatis unde omnis</h3><p>Ut enim ad minima veniam, quis nostrum exercitationem ullamtu corporis suscipit laboriosam, utt nisi ut aliquid ex ea commod.</p></article>
<article class="post" style="left:779px"><div class="pic" role="img" aria-label="Business people in a meeting around a laptop"><span class="date">12 Jan 2024</span></div><h3>Sed ut perspiciatis unde omnis</h3><p>Ut enim ad minima veniam, quis nostrum exercitationem ullamtu corporis suscipit laboriosam, utt nisi ut aliquid ex ea commod.</p></article>

<footer class="footer">
  <h4 style="left:98px">Quick Links</h4>
  <ul class="links">
    <li>&#10140; Home</li><li>&#10140; Analyze Log Files</li><li>&#10140; Subscribe</li><li>&#10140; About Us</li><li>&#10140; FAQ</li><li>&#10140; Contact Us</li>
  </ul>
  <div class="social" aria-label="Social links"><span></span><span></span><span></span><span></span></div>
  <div class="divider" style="left:302px"></div>

  <h4 style="left:355px">Contact Details</h4>
  <div class="contact" style="top:110px"><span class="ic"><svg width="14" height="14" viewBox="0 0 24 24"><path fill="#fff" d="M6.6 10.8a15 15 0 0 0 6.6 6.6l2.2-2.2c.3-.3.7-.4 1-.2 1.1.4 2.3.6 3.6.6.6 0 1 .4 1 1V20c0 .6-.4 1-1 1A17 17 0 0 1 3 4c0-.6.4-1 1-1h3.5c.6 0 1 .4 1 1 0 1.3.2 2.5.6 3.6.1.3 0 .7-.2 1z"/></svg></span><div><b>Phone:</b><span>+1 555 0142 7788</span></div></div>
  <div class="contact-sep" style="top:177px"></div>
  <div class="contact" style="top:192px"><span class="ic"><svg width="14" height="12" viewBox="0 0 24 20"><rect x="1" y="1" width="22" height="18" fill="#fff"/><path d="M1 1l11 9 11-9" stroke="#ee3b48" stroke-width="2" fill="none"/></svg></span><div><b>Email:</b><span>hello@trackmindlens.example</span></div></div>
  <div class="contact-sep" style="top:258px"></div>
  <div class="contact" style="top:274px"><span class="ic"><svg width="12" height="16" viewBox="0 0 12 16"><path fill="#fff" d="M6 0a6 6 0 0 0-6 6c0 4.5 6 10 6 10s6-5.5 6-10a6 6 0 0 0-6-6zm0 8.5A2.5 2.5 0 1 1 6 3.5a2.5 2.5 0 0 1 0 5z"/></svg></span><div><b>Address:</b><span>Company Name,United State.</span></div></div>
  <div class="divider" style="left:670px"></div>

  <h4 style="left:715px">Contact Me</h4>
  <div class="form">
    <div class="field">Name:</div><div class="field">Email:</div><div class="field">Address:</div>
    <div class="submit">Submit Now</div>
  </div>
  <div class="copy">Copyrights@2024.TrackMind Lens.All Rights Reserved</div>
</footer>

</body>
</html>
```